Unique business card design

We are looking for a design that reflects our unique social media and online marketing agency "Kestrel Media". We are a young agency with a focus on speakers, coaches and trainers. In other words, we support people who want to do good with their work and help other people live a happier, more successful and fulfilling life, reach as many people as possible with their work and thus have an influence. Our values are: sustainability, creating added value, individuality, proactivity. We want our clients to feel comfortable with us and that's why the relationship with them is very important to us. We want every customer to become a lifelong friend of the company. Most of our clients are premium coaches, meaning they are in the higher priced segment and expect seriousness, professionalism and quality. All of these things should reflect our business card as well. I look forward to feedback. Best regards, Tomas Wylander

```html
<!DOCTYPE html>
<html lang="en">
<head>
<meta charset="utf-8">
<title>Kestrel Media – Business Card</title>
<link rel="stylesheet" href="https://fonts.googleapis.com/css2?family=Saira+Condensed:wght@300;400;700&display=swap">
<style>
  :root {
    --backdrop: #eceeed;
    --card-white: #ffffff;
    --ice-blue: #b9d6ee;
    --sky-blue: #8db8df;
    --brand-blue: #1a72ba;
    --brand-blue-light: #2784c9;
    --navy: #1d2a78;
    --text-white: #ffffff;
    --values-blue: #86b8e4;
  }
  * { margin: 0; padding: 0; box-sizing: border-box; }
  html, body {
    width: 1200px;
    height: 1200px;
    overflow: hidden;
    background: var(--backdrop);
    font-family: "Saira Condensed", "Arial Narrow", sans-serif;
  }
  .card {
    position: absolute;
    top: 276px;
    width: 358px;
    height: 628px;
  }
  .card-front {
    left: 198px;
    background: var(--card-white);
    overflow: hidden;
  }
  .front-artwork {
    position: absolute;
    inset: 0;
    background:
      linear-gradient(200deg, var(--sky-blue) 0%, rgba(185,214,238,0.7) 35%, rgba(255,255,255,0) 70%),
      linear-gradient(160deg, var(--card-white) 30%, var(--ice-blue) 100%);
  }
  .brand {
    position: absolute;
    left: 47px;
    bottom: 70px;
    display: flex;
    align-items: center;
    gap: 12px;
  }
  .brand-square {
    width: 34px;
    height: 34px;
    background: var(--navy);
  }
  .brand-name {
    font-size: 38px;
    font-weight: 400;
    line-height: 1;
    color: var(--navy);
  }
  .card-back {
    left: 632px;
    background: radial-gradient(ellipse 60% 55% at 40% 45%, var(--brand-blue-light) 0%, var(--brand-blue) 100%);
    color: var(--text-white);
  }
  .person {
    position: absolute;
    left: 37px;
    top: 55px;
    line-height: 1;
  }
  .person-first {
    display: block;
    font-size: 22px;
    font-weight: 300;
  }
  .person-last {
    display: block;
    font-size: 25px;
    font-weight: 700;
    letter-spacing: 0.3px;
  }
  .contact {
    position: absolute;
    left: 37px;
    top: 422px;
    font-size: 21px;
    font-weight: 400;
    line-height: 27px;
    font-style: normal;
  }
  .values {
    margin-top: 3px;
    color: var(--values-blue);
    font-weight: 300;
  }
  .values .dot { margin: 0 6px; font-size: 14px; vertical-align: 2px; }
</style>
</head>
<body>
  <section class="card card-front">
    <div class="front-artwork" role="img" aria-label="Abstract pattern of overlapping translucent light-blue light beams"></div>
    <div class="brand">
      <span class="brand-square"></span>
      <span class="brand-name">Kestrel Media</span>
    </div>
  </section>

  <section class="card card-back">
    <h1 class="person">
      <span class="person-first">Tomas</span>
      <span class="person-last">WYLANDER</span>
    </h1>
    <address class="contact">
      <div>42 Lindenweg</div>
      <div>53119 Bonn</div>
      <div>T.02741 38 16 02</div>
      <div>M.02741 90 57 44</div>
      <div>wylander@kestrelmedia.com</div>
      <div class="values">value<span class="dot">•</span>sustainability<span class="dot">•</span>individuality</div>
    </address>
  </section>
</body>
</html>
```